Label for packaging - front and back

Hello,
We are looking for a fresh design based off of the current one we have. We need something fresh simple and eye catching. Company is VerdanKelpa.com I am including current packaging and also a trim fold fliers we had made.
VK Brochure is what we could use as design inspiration perhaps?
Updates
PLEASE replace super food with " Past Mighty Greens". somewhere on the label. In addition, please include website name on front.
Target Market(s)
Nutrition, athletes, anyone who wants to improve health
Look and feel
Each slider illustrates characteristics of the customer's brand and the style your logo design should communicate.

```html
<!DOCTYPE html>
<html lang="en">
<head>
<meta charset="utf-8">
<title>Verdan Kelpa – Spirulina Platensis Label</title>
<link rel="stylesheet" href="https://fonts.googleapis.com/css2?family=Montserrat:wght@300;500;600;700&family=Cabin:wght@400&display=swap">
<style>
  :root {
    --backdrop: #424242;
    --paper: #ffffff;
    --leaf-green: #689a3a;
    --deep-green: #4f8a2e;
    --navy: #1c2440;
    --ink: #111111;
    --powder: #8fc23f;
    --powder-light: #d6ebb0;
  }
  * { margin: 0; padding: 0; box-sizing: border-box; }
  html, body {
    width: 1074px; height: 1200px; overflow: hidden;
    background: var(--backdrop);
  }
  .label {
    position: absolute; left: 240px; top: 173px;
    width: 595px; height: 854px;
    background: var(--paper);
    box-shadow: 0 4px 10px rgba(0,0,0,.35);
    overflow: hidden;
    font-family: "Montserrat", sans-serif;
  }
  .brand {
    position: absolute; top: 72px; left: 0; width: 100%;
    display: flex; justify-content: center; align-items: center; gap: 14px;
  }
  .brand-dot {
    width: 40px; height: 40px; border-radius: 50%;
    background: var(--leaf-green);
  }
  .brand-name {
    font-family: "Montserrat", sans-serif; font-weight: 500;
    font-size: 24px; letter-spacing: 4px; color: var(--navy);
  }
  .title-band {
    position: absolute; left: 0; top: 176px; width: 100%; height: 166px;
    background: var(--leaf-green); color: var(--paper); text-align: center;
  }
  .title-main {
    position: absolute; top: 10px; width: 100%;
    font-weight: 600; font-size: 66px; line-height: 1; letter-spacing: 1px;
  }
  .title-sub {
    position: absolute; top: 70px; width: 100%;
    font-weight: 300; font-size: 56px; line-height: 1;
  }
  .tagline {
    position: absolute; top: 134px; width: 100%;
    font-weight: 600; font-size: 13.5px; letter-spacing: 1.6px;
  }
  .product-photo {
    position: absolute; left: 0; top: 440px; width: 100%; height: 414px;
    background:
      radial-gradient(ellipse 42% 30% at 54% 40%, var(--powder) 0%, rgba(143,194,63,.75) 45%, rgba(214,235,176,0) 100%),
      radial-gradient(ellipse 60% 22% at 60% 72%, rgba(143,194,63,.6) 0%, rgba(214,235,176,0) 100%),
      linear-gradient(var(--paper), #f3f5f1);
  }
  .claims-heading {
    position: absolute; top: 362px; width: 100%; text-align: center;
    font-weight: 700; font-size: 20px; color: var(--deep-green);
  }
  .benefits-divider {
    position: absolute; left: 296px; top: 394px; width: 1.5px; height: 92px;
    background: var(--deep-green);
  }
  .benefit-icon { position: absolute; width: 44px; height: 44px; }
  .benefit-text {
    position: absolute; width: 120px;
    font-family: "Cabin", sans-serif; font-size: 10.5px; line-height: 1.05;
    color: var(--deep-green);
  }
  .benefit-text.left { text-align: right; left: 111px; }
  .benefit-text.right { text-align: left; left: 362px; }
  .highlights {
    position: absolute; left: 38px; top: 653px; list-style: none;
  }
  .highlights li {
    display: flex; align-items: center; gap: 6px; height: 30px;
    font-weight: 700; font-size: 15px; color: var(--deep-green);
  }
  .website {
    position: absolute; left: 38px; top: 800px;
    font-weight: 500; font-size: 12.5px; color: var(--deep-green);
  }
  .net-weight {
    position: absolute; left: 462px; top: 766px; text-align: center; color: var(--ink);
  }
  .net-weight .label-text { font-weight: 500; font-size: 12px; letter-spacing: 1.3px; }
  .net-weight .amount { font-weight: 600; font-size: 40px; line-height: 1; letter-spacing: -1px; }
</style>
</head>
<body>
  <main class="label">
    <div class="brand">
      <span class="brand-dot"></span>
      <span class="brand-name">VERDAN KELPA</span>
    </div>

    <section class="title-band">
      <h1 class="title-main">SPIRULINA</h1>
      <p class="title-sub">Platensis</p>
      <p class="tagline">FREEZE DRIED TO PRESERVE ALL NUTRITION</p>
    </section>

    <div class="product-photo" role="img" aria-label="Heap of green spirulina powder on a white ceramic spoon with powder scattered around"></div>

    <h2 class="claims-heading">Past Mighty Greens</h2>

    <p class="benefit-text left" style="top:407px">Excellent source of zinc to boost your immune system.</p>
    <svg class="benefit-icon" style="left:238px;top:399px" viewBox="0 0 44 44" aria-hidden="true">
      <circle cx="22" cy="22" r="20.5" fill="none" stroke="#4f8a2e" stroke-width="2"/>
      <g stroke="#4f8a2e" stroke-width="2.2" fill="#4f8a2e">
        <line x1="13" y1="15" x2="22" y2="22"/><line x1="22" y1="22" x2="30" y2="15"/>
        <line x1="22" y1="22" x2="14" y2="29"/><line x1="22" y1="22" x2="30" y2="25"/>
        <circle cx="22" cy="22" r="3.5"/><circle cx="13" cy="15" r="2.5"/>
        <circle cx="30" cy="15" r="2.5"/><circle cx="14" cy="29" r="2.5"/><circle cx="31" cy="26" r="3.5"/>
      </g>
    </svg>

    <svg class="benefit-icon" style="left:310px;top:397px" viewBox="0 0 44 44" aria-hidden="true">
      <circle cx="22" cy="22" r="20.5" fill="none" stroke="#4f8a2e" stroke-width="2"/>
      <path d="M22 31 C12 24 11 17 15.5 14.5 C18.5 13 21 14.5 22 17 C23 14.5 25.5 13 28.5 14.5 C33 17 32 24 22 31Z" fill="none" stroke="#4f8a2e" stroke-width="2"/>
      <polyline points="15,21 19,21 20.5,18 22.5,24 24,20 29,20" fill="none" stroke="#4f8a2e" stroke-width="1.5"/>
    </svg>
    <p class="benefit-text right" style="top:406px">Powerful source of antioxidants and protein</p>

    <p class="benefit-text left" style="top:459px">Vitamins B1, B2, B3, B5, B6, B7, B8, B9, C, D, E and K.</p>
    <svg class="benefit-icon" style="left:238px;top:451px" viewBox="0 0 44 44" aria-hidden="true">
      <circle cx="22" cy="22" r="20.5" fill="none" stroke="#4f8a2e" stroke-width="2"/>
      <path d="M13 31 L13 20 C13 15 16 12 20 12 L23 12 L23 16 L19 18 L19 24 C22 21 28 21 31 25 C33 29 30 32 26 32 Z" fill="#4f8a2e"/>
    </svg>

    <svg class="benefit-icon" style="left:310px;top:451px" viewBox="0 0 44 44" aria-hidden="true">
      <circle cx="22" cy="22" r="20.5" fill="none" stroke="#4f8a2e" stroke-width="2"/>
      <path d="M15 29 C14 19 21 13 31 13 C31 23 25 29 15 29Z" fill="#4f8a2e"/>
      <path d="M12 33 L26 18" stroke="#ffffff" stroke-width="1.6"/>
    </svg>
    <p class="benefit-text right" style="top:468px">Rich in chlorophyll</p>

    <div class="benefits-divider"></div>

    <ul class="highlights">
      <li><svg width="20" height="20" viewBox="0 0 20 20" aria-hidden="true"><path d="M17 8.5 A7.5 7.5 0 1 1 13 3.2" fill="none" stroke="#4f8a2e" stroke-width="1.8"/><polyline points="6,9.5 9.5,13 18,3.5" fill="none" stroke="#4f8a2e" stroke-width="2"/></svg>PROTIN 70%</li>
      <li><svg width="20" height="20" viewBox="0 0 20 20" aria-hidden="true"><path d="M17 8.5 A7.5 7.5 0 1 1 13 3.2" fill="none" stroke="#4f8a2e" stroke-width="1.8"/><polyline points="6,9.5 9.5,13 18,3.5" fill="none" stroke="#4f8a2e" stroke-width="2"/></svg>AMINO ACID19</li>
      <li><svg width="20" height="20" viewBox="0 0 20 20" aria-hidden="true"><path d="M17 8.5 A7.5 7.5 0 1 1 13 3.2" fill="none" stroke="#4f8a2e" stroke-width="1.8"/><polyline points="6,9.5 9.5,13 18,3.5" fill="none" stroke="#4f8a2e" stroke-width="2"/></svg>VITAMINS</li>
    </ul>

    <p class="website">www.VerdanKelpa.com</p>

    <div class="net-weight">
      <p class="label-text">Net Weight</p>
      <p class="amount">120g</p>
    </div>
  </main>
</body>
</html>
```